I need a business card design for my new clinic (SPORTS MEDICINE OF KNEE). I am orthopedist, expert in sports surgery, especially knee surgery. I prefer, as colors, the colors of my logo (green, black and white). I already have my logo and should appear on my card. It's good to see my site to have ideas (www.drlucianovarela.com)
It needs contain:
my name: Dr. Luciano Varela
my registration: CRM 584-902
my specialty: Cirurgia do Joelho / Esporte
my address: Centro Executivo - Pinheiral Plaza
Av. Doutor Augusto Brandão Cunha, 2740 sala 0836
Jd. Ipanema - Ribeirão Preto - SP
my phone number: Tel (16) 8245-3908
my clinic phone: (16) 3670-4851
my e-mail: drlucianovarela@mailbox-exemplo.com
my site: www.drlucianovarela.com

Target Market(s)

futures patients

Industry/Entity Type

Clinic

Requirements
Nice to have
• letters not overfilled
straight lines, with few curves

```html
<!DOCTYPE html>
<html lang="pt-BR">
<head>
<meta charset="utf-8">
<title>Dr. Luciano Varela – Cartão</title>
<link href="https://fonts.googleapis.com/css2?family=Arimo:wght@400;700&display=swap" rel="stylesheet">
<style>
  :root {
    --green: #46bd7c;
    --green-faint: #5cc78c;
    --ink: #0d0d0d;
    --paper: #ffffff;
    --edge: #151515;
  }
  html, body {
    margin: 0;
    padding: 0;
    overflow: hidden;
    background: var(--paper);
  }
  .card {
    position: relative;
    width: 1200px;
    height: 900px;
    overflow: hidden;
    background: var(--paper);
    font-family: "Arimo", Arial, sans-serif;
    color: var(--ink);
  }
  .card__shape {
    position: absolute;
    inset: 0;
  }
  .brand {
    position: absolute;
    top: 14px;
    right: 40px;
    display: flex;
    align-items: center;
    gap: 14px;
  }
  .brand__mark {
    width: 86px;
    height: 104px;
    background: var(--ink);
    border-radius: 8px;
  }
  .brand__name {
    font-weight: 400;
    color: var(--ink);
    line-height: 1;
  }
  .brand__name-main {
    display: block;
    font-size: 76px;
    letter-spacing: 1px;
  }
  .brand__name-sub {
    display: block;
    font-size: 21px;
    margin-top: 6px;
    text-align: right;
  }
  .backdrop-name {
    position: absolute;
    left: 500px;
    top: 300px;
    font-size: 190px;
    font-weight: 400;
    color: var(--green-faint);
    transform: rotate(12deg);
    transform-origin: left top;
    letter-spacing: 4px;
    line-height: 1;
  }
  .registration {
    position: absolute;
    left: 42px;
    top: 44px;
    margin: 0;
    font-size: 31px;
    font-weight: 700;
  }
  .identity, .contact {
    position: absolute;
    left: 32px;
    margin: 0;
    font-size: 31px;
    font-weight: 700;
    line-height: 48px;
  }
  .identity { top: 345px; }
  .identity .identity__name { padding-left: 4px; }
  .contact { top: 641px; }
  .contact .contact__addr { padding-left: 8px; }
  .contact span { display: block; }
  .identity span { display: block; }
</style>
</head>
<body>
<main class="card">
  <svg class="card__shape" width="1200" height="900" viewBox="0 0 1200 900" aria-hidden="true">
    <path d="M22 0 H430 C770 110 1080 450 1178 812 V900 H22 Z" fill="var(--green)"/>
    <rect x="1178" y="0" width="22" height="900" fill="var(--edge)"/>
  </svg>

  <div class="backdrop-name" aria-hidden="true">VARELA</div>

  <p class="registration">CRM 584-902</p>

  <div class="brand">
    <div class="brand__mark" aria-hidden="true"></div>
    <div class="brand__name">
      <span class="brand__name-main">VARELA</span>
      <span class="brand__name-sub">Traumatologia Esportiva</span>
    </div>
  </div>

  <p class="identity">
    <span class="identity__name">Dr. Luciano Varela</span>
    <span>Centro Executivo - Pinheiral Plaza</span>
    <span>Cirurgia do Joelho / Esporte</span>
  </p>

  <p class="contact">
    <span class="contact__addr">Av. Doutor Augusto Brandão Cunha, 2740 sala 0836</span>
    <span class="contact__addr">Jd. Ipanema - Ribeirão Preto - SP</span>
    <span>Tel (16) 8245-3908, (16) 3670-4851</span>
    <span>drlucianovarela@mailbox-exemplo.com</span>
    <span>www.drlucianovarela.com</span>
  </p>
</main>
</body>
</html>
```